Plakat-Design für Vereinsfest
Zielgruppe
Unser Verein veranstaltet jedes Jahr im August das Vereinsfest 'Sonnenklang', das in einem kleinen Wäldchen innerhalb des Heimatortes stattfindet. Am Samstag und Sonntag sorgen verschiedene Musikgruppen für Unterhaltung. Es soll ein Veranstaltungsplakat gestaltet werden, dass sich an die Vorgaben (siehe unten) hält und die Veranstaltung bewirbt.
Zielgruppe sind Bürger des Heimatortes.
Aufgabenstellung
Das Vereinslogo ist beigefügt und sollte prominent auf dem Plakat vertreten sein, Logo und Schriftzug können auch getrennt oder anders angeordnet werden. Der Veranstaltungstitel lautet "Sonnenklang", es findet am 20. und 21. August "Am Ressleberg" (Veranstaltungsort) statt.
Programmpunkte: Samstag: Musikalische Unterhaltung mit den Kolbenbrüdern; Sonntag: Musikalische Unterhaltung mit den Moorhügelrappeln
Uhrzeiten sollten enthalten sein:
Beginn Samstag: ab 15 Uhr
Beginn Sonntag: ab 10 Uhr
Das Plakat soll gut leserlich auch aus der Entfernung sein, da es an Straßen plakatiert wird.
Das Plakat soll für spätere Jahre editierbar sein.
Schriftart im Logo: Californian FB Bold (muss aber nicht auf andere Textelemente angewendet werden). Das Plakat soll in DIN A2 gedruckt werden. Die Webadresse sollte auf dem Plakat stehen.

```html
<!DOCTYPE html>
<html lang="de">
<head>
<meta charset="utf-8">
<title>Sonnenklang – Am Ressleberg</title>
<link href="https://fonts.googleapis.com/css2?family=Rye&family=Open+Sans:wght@400;700&family=Libre+Caslon+Text:wght@700&display=swap" rel="stylesheet">
<style>
  :root {
    --wood-dark: #2e1a0d;
    --wood-mid: #4e3019;
    --wood-light: #65412a;
    --cream: #f6e4c4;
    --gold: #c99a5c;
    --tan: #e2bb82;
    --orange: #d9651c;
    --outline: #2a1608;
    --white: #ffffff;
    --brass: #b8985a;
    --spruce: #c98b4a;
    --black-inst: #1b1716;
    --chrome: #a7a7a7;
    --redwood: #6a2a1e;
  }
  * { margin: 0; padding: 0; box-sizing: border-box; }
  html, body { width: 853px; height: 1200px; overflow: hidden; background: var(--wood-dark); }
  .poster {
    position: relative;
    width: 853px;
    height: 1200px;
    overflow: hidden;
    background:
      radial-gradient(ellipse at 50% 45%, var(--wood-light) 0%, var(--wood-mid) 45%, var(--wood-dark) 100%);
    font-family: "Open Sans", Arial, sans-serif;
  }

  /* club name */
  .club {
    position: absolute;
    left: 288px;
    top: 18px;
    display: flex;
    align-items: center;
    gap: 10px;
  }
  .club-dot {
    width: 64px; height: 64px;
    border-radius: 50%;
    background: var(--gold);
    flex: none;
  }
  .club-name {
    font-family: "Libre Caslon Text", Georgia, serif;
    font-weight: 700;
    color: var(--tan);
    font-size: 19px;
    line-height: 19px;
  }
  .club-name small { display: block; font-size: 10px; line-height: 12px; }

  .slogan {
    position: absolute;
    left: 560px;
    top: 62px;
    transform: rotate(12deg);
    transform-origin: left top;
    font-family: "Rye", Georgia, serif;
    color: #8a6440;
    text-align: center;
    line-height: 1;
  }
  .slogan-big { font-size: 46px; display: block; }
  .slogan-small { font-size: 15px; display: block; margin-left: -10px; }

  .headline { position: absolute; left: 0; top: 0; }

  /* instrument artwork placeholders */
  .art { position: absolute; }
  .art-horn {
    left: -40px; top: 318px; width: 240px; height: 370px;
    border-radius: 0 60% 50% 0;
    background: radial-gradient(circle at 45% 40%, #e3cf96 0%, var(--brass) 45%, #5f4a25 100%);
  }
  .art-guitar-left {
    left: -30px; top: 740px; width: 170px; height: 230px;
    border-radius: 48% 48% 45% 45%;
    background: radial-gradient(circle at 50% 45%, #f0b46a 0%, var(--spruce) 55%, #6d3d1b 100%);
  }
  .art-guitar-neck-left {
    left: 72px; top: 540px; width: 26px; height: 210px;
    transform: rotate(8deg);
    background: linear-gradient(#2a201a, #4a3a2c);
  }
  .art-mic {
    left: -10px; top: 985px; width: 120px; height: 215px;
    border-radius: 55px 55px 10px 10px;
    background: linear-gradient(90deg, #5e5e5e, #d7d7d7 55%, #777);
  }
  .art-accordion {
    left: 608px; top: 292px; width: 260px; height: 320px;
    border-radius: 10px 0 0 10px;
    background: linear-gradient(100deg, #efefef 0 22%, var(--black-inst) 22% 60%, #3a3a3a 100%);
  }
  .art-guitar-right {
    left: 695px; top: 720px; width: 170px; height: 255px;
    border-radius: 50% 30% 40% 45%;
    background: radial-gradient(circle at 55% 45%, #3b3535 0%, var(--black-inst) 70%);
  }
  .art-guitar-neck-right {
    left: 712px; top: 487px; width: 22px; height: 250px;
    transform: rotate(-6deg);
    background: linear-gradient(#2a2020, #40302c);
  }
  .art-bandoneon {
    left: 585px; top: 958px; width: 290px; height: 260px;
    border-radius: 18px;
    transform: rotate(-8deg);
    background: linear-gradient(135deg, #b3a79c 0%, var(--redwood) 45%, #3e1812 100%);
  }

  .program-title { position: absolute; left: 0; top: 0; }

  .program {
    position: absolute;
    left: 0;
    width: 853px;
    text-align: center;
    color: var(--white);
    font-weight: 700;
    font-size: 27.5px;
    line-height: 40.5px;
  }
  .program-sat { top: 504px; }
  .program-sun { top: 713px; }

  .tagline {
    position: absolute;
    left: 0;
    top: 998px;
    width: 853px;
    text-align: center;
    font-family: "Rye", Georgia, serif;
    color: var(--orange);
    font-size: 38px;
    line-height: 46px;
    transform: rotate(-2deg);
  }

  .web {
    position: absolute;
    left: 0;
    top: 1140px;
    width: 853px;
    text-align: center;
    color: var(--tan);
    font-size: 29px;
    padding-left: 10px;
  }
</style>
</head>
<body>
<div class="poster">

  <div class="art art-horn" role="img" aria-label="Foto eines Waldhorns"></div>
  <div class="art art-guitar-neck-left" role="img" aria-label="Hals einer Akustikgitarre"></div>
  <div class="art art-guitar-left" role="img" aria-label="Foto einer Akustikgitarre"></div>
  <div class="art art-mic" role="img" aria-label="Foto eines Retro-Mikrofons"></div>
  <div class="art art-accordion" role="img" aria-label="Foto eines Akkordeons"></div>
  <div class="art art-guitar-neck-right" role="img" aria-label="Hals einer schwarzen Gitarre"></div>
  <div class="art art-guitar-right" role="img" aria-label="Foto einer schwarzen Westerngitarre"></div>
  <div class="art art-bandoneon" role="img" aria-label="Foto einer verzierten Konzertina"></div>

  <div class="club">
    <span class="club-dot"></span>
    <span class="club-name"><small>Historische</small>Schützengilde und<br>Trachtengruppe<br>Talheim e.V.</span>
  </div>

  <div class="slogan">
    <span class="slogan-big">Gute</span>
    <span class="slogan-small">Unterhaltung!</span>
  </div>

  <svg class="headline" width="853" height="360" viewBox="0 0 853 360">
    <defs>
      <linearGradient id="titleFill" x1="0" y1="0" x2="0" y2="1">
        <stop offset="0" stop-color="#fbf0da"/>
        <stop offset="0.55" stop-color="#f1d9ae"/>
        <stop offset="1" stop-color="#c99a5c"/>
      </linearGradient>
    </defs>
    <text class="title-main" x="60" y="268" textLength="735" lengthAdjust="spacingAndGlyphs"
          font-family="Rye, Georgia, serif" font-size="150"
          fill="url(#titleFill)" stroke="var(--outline)" stroke-width="5" paint-order="stroke">Sonnenklang</text>
    <text class="title-venue" x="190" y="340" textLength="475" lengthAdjust="spacingAndGlyphs"
          font-family="Rye, Georgia, serif" font-size="56"
          fill="var(--orange)" stroke="var(--outline)" stroke-width="4" paint-order="stroke">Am Ressleberg</text>
  </svg>

  <svg class="program-title" width="853" height="460" viewBox="0 0 853 460">
    <text x="256" y="440" textLength="344" lengthAdjust="spacingAndGlyphs"
          font-family="Rye, Georgia, serif" font-size="44" fill="var(--tan)">Das Programm</text>
  </svg>

  <p class="program program-sat">Samstag, 20. August 2016,<br>ab 15 Uhr<br>Musikalische Unterhaltung mit<br>den „Kolbenbrüdern“</p>

  <p class="program program-sun">Sonntag, 21 August 2016,<br>ab 10 Uhr<br>Stimmung pur mit den<br>„Moorhügelrappeln“</p>

  <p class="tagline">Mehr Stimmung<br>geht nicht!!!</p>

  <p class="web">www.schuetzengilde-talheim.de</p>
</div>
</body>
</html>
```